Verostel business card

Business card for sustainable investment company called "Verostel". Verostel is an exchange platform selling carbon credits between buyers and sellers. Carbon Credits are an environmental commodity for reducing global carbon emissions.

the card should obviously have our logo and the theme should be sustainability/environment mixed with a trading platform.

Contact Information for Business Card

Logo, Name, Title, Phone, Email

Colors
0054AA
0677BA
7BADD7
CADEEF
E8F1F8
0094D4
00A9DD
6FCCEA
C7EBF8
E9F6FB
00AB8E
00BBA5
67D7C9
C6EFE9
E9F9F6
59FF00
82FF00
B8FF75
E3FFCB
F4FFEA

```html
<!DOCTYPE html>
<html lang="en">
<head>
<meta charset="utf-8">
<title>Verostel business card</title>
<link href="https://fonts.googleapis.com/css2?family=Montserrat:wght@400;600;700&display=swap" rel="stylesheet">
<style>
  :root{
    --page:#e6e8eb;
    --card:#fbfbfb;
    --ink:#1c2b45;
    --blue-deep:#1f6fe0;
    --cyan:#45dbe8;
    --blue:#2a86e6;
    --text:#1a1a1a;
  }
  *{margin:0;padding:0;box-sizing:border-box}
  html,body{width:1200px;height:768px;overflow:hidden}
  body{
    background:var(--page);
    font-family:"Montserrat",Arial,sans-serif;
    display:flex;align-items:center;justify-content:center;gap:48px;
  }
  .card{
    position:relative;
    width:540px;height:310px;
    background:var(--card);
    border-radius:22px;
    box-shadow:0 10px 30px rgba(0,0,0,.12);
    overflow:hidden;
  }
  /* front */
  .card--front{display:flex;align-items:center;justify-content:center;gap:16px}
  .brand-dot{
    width:34px;height:34px;border-radius:50%;
    background:linear-gradient(135deg,var(--cyan),var(--blue-deep));
  }
  .brand-name{
    font-weight:700;font-size:40px;letter-spacing:2px;color:var(--ink);
  }
  /* back */
  .back-brand{
    position:absolute;left:38px;top:32px;
    font-weight:700;font-size:22px;letter-spacing:1.5px;color:var(--ink);
  }
  .back-mark{
    position:absolute;right:40px;top:48px;
    width:250px;height:250px;border-radius:50%;
    background:linear-gradient(135deg,var(--cyan),var(--blue-deep));
  }
  .person{
    position:absolute;right:70px;top:150px;width:190px;
    color:#fff;
  }
  .person__name{font-weight:700;font-size:24px;line-height:1.1}
  .person__title{font-weight:600;font-size:15px;margin-top:2px}
  .contact{
    position:absolute;left:38px;bottom:48px;
    font-weight:400;font-size:15px;line-height:1.45;color:var(--text);
  }
</style>
</head>
<body>
  <section class="card card--front">
    <span class="brand-dot"></span>
    <span class="brand-name">VEROSTEL</span>
  </section>

  <section class="card card--back">
    <div class="back-brand">VEROSTEL</div>
    <div class="back-mark"></div>
    <div class="person">
      <div class="person__name">Marcus Hale</div>
      <div class="person__title">President</div>
    </div>
    <div class="contact">
      <div>(555) 0142-7789</div>
      <div>info@verostel.com</div>
    </div>
  </section>
</body>
</html>
```